Business Card Design for Cloud Frames

Hi we need a business card designed for a new aerial photography business we have started, we use UAV Drones to take photos for corporate, events, real estate, local government etc , the business name is Cloud Frames Australia, we have a facebook page that might help you come up with some designs - https://www.facebook.com/cloudframesaustralia

We need to have and editable AI file so that we can use different names and contact details. details for one of the cards as follow:

Dave Marsh
phone: 03 5512 4837
Mobile: 0439 175 286
email: dave@cloudframes.example.com.au
web: www.cloudframes.example.com.au

have now changed: Designer Payment:Committed

Target Market(s)

We are a Aerial Photography business using Drones and UAV

Industry/Entity Type

Business

Logo Text

Cloud Frames Australia

Requirements
Must have
• Colors to match logo and be part of Cloud Frames Brand

```html
<!DOCTYPE html>
<html lang="en">
<head>
<meta charset="utf-8">
<title>Cloud Frames Australia — Business Card</title>
<link href="https://fonts.googleapis.com/css2?family=Mulish:wght@400;600;800&display=swap" rel="stylesheet">
<style>
  :root {
    --backdrop: #d7d8da;
    --card-white: #f4f4f5;
    --brand-blue: #2aa4de;
    --sky-blue: #45b6ea;
    --sky-pale: #7ccbef;
    --ink: #1d1d1f;
    --rule: #8f9194;
    --shadow: rgba(40, 44, 52, 0.22);
  }
  * { box-sizing: border-box; margin: 0; padding: 0; }
  html, body { width: 1200px; height: 900px; overflow: hidden; }
  body {
    background: var(--backdrop);
    font-family: "Mulish", Arial, sans-serif;
    display: flex;
    align-items: center;
    justify-content: center;
    gap: 40px;
  }
  .card {
    position: relative;
    width: 540px;
    height: 309px;
    border-radius: 26px;
    overflow: hidden;
    box-shadow: 0 10px 28px var(--shadow);
  }

  /* Front */
  .card-front { background: var(--card-white); }
  .wordmark {
    font-weight: 800;
    color: var(--ink);
    text-transform: uppercase;
    line-height: 1;
  }
  .card-front .wordmark {
    position: absolute;
    right: 40px;
    top: 46px;
    text-align: right;
  }
  .wordmark .name { font-size: 30px; letter-spacing: 1px; display: block; }
  .wordmark .region { font-size: 12px; letter-spacing: 7px; display: block; margin-top: 6px; }
  .rule-top {
    position: absolute;
    left: 250px; right: 34px; top: 138px;
    height: 1px; background: var(--rule);
  }
  .holder {
    position: absolute;
    left: 40px; top: 190px;
    font-size: 24px;
    font-weight: 400;
    letter-spacing: 0.5px;
    color: var(--brand-blue);
    text-transform: uppercase;
  }
  .rule-name {
    position: absolute;
    left: 40px; width: 210px; top: 228px;
    height: 1px; background: var(--rule);
  }
  .contact {
    position: absolute;
    list-style: none;
    font-size: 13px;
    line-height: 1.55;
    color: var(--ink);
  }
  .contact .label { color: var(--brand-blue); font-size: 10.5px; text-transform: uppercase; }
  .contact-phones { left: 52px; top: 236px; }
  .contact-online { left: 262px; top: 160px; font-size: 12px; }

  /* Back */
  .card-back { background: var(--sky-blue); }
  .scene-photo {
    position: absolute;
    left: 0; right: 0; top: 0;
    height: 178px;
    background: linear-gradient(180deg, var(--sky-pale) 0%, #5cbfec 55%, var(--sky-blue) 100%);
  }
  .card-back .wordmark {
    position: absolute;
    left: 40px; bottom: 42px;
  }
</style>
</head>
<body>
  <section class="card card-front" aria-label="Business card front">
    <div class="wordmark">
      <span class="name">Cloud Frames</span>
      <span class="region">Australia</span>
    </div>
    <div class="rule-top"></div>
    <h1 class="holder">Dave Marsh</h1>
    <div class="rule-name"></div>
    <ul class="contact contact-phones">
      <li><span class="label">Phone:</span> 03 5512 4837</li>
      <li><span class="label">Mobile:</span> 0439 175 286</li>
    </ul>
    <ul class="contact contact-online">
      <li><span class="label">Email:</span> dave@cloudframes.example.com.au</li>
      <li><span class="label">Web:</span> www.cloudframes.example.com.au</li>
    </ul>
  </section>

  <section class="card card-back" aria-label="Business card back">
    <div class="scene-photo" role="img" aria-label="Blue-tinted photograph of a city skyline across a lake with trees"></div>
    <div class="wordmark">
      <span class="name">Cloud Frames</span>
      <span class="region">Australia</span>
    </div>
  </section>
</body>
</html>
```